Law Firm Website

We are a small California based law firm specializing in business, corporate and litigation matters. We need to have our website redesigned. We are looking for a new and fresh look for our site, keeping in mind that we are a law firm.
What we don't want:
**the traditional "gavel" and "scales of justice" look
**anything too crazy
What we do want:
**sophisticated yet modern and fresh corporate look and feel
**samples of websites we really like:
http://www.mtrhllp-example.com
http://www.orwenlatch-example.com/
we also like:
http://www.verdtolbain-example.com/
http://www.qh-example.com/
http://www.pembrost-example.com/
http://www.nvtr-example.com
http://www.rmqlaw-example.com/
The content will be whatever is currently on our website (www.halvencourtlaw-example.com). We will be selecting the winner based on originality and keeping the above requirements in mind. Please note that the photos that you use will be the ones that we will be using, so choose wisely because the photos will make a difference.
Target Market(s)
Corporate clients
Industry/Entity Type
Law Firm
Look and feel

```html
<!DOCTYPE html>
<html lang="en">
<head>
<meta charset="utf-8">
<title>Halvencourt Law Group, LLP</title>
<link href="https://fonts.googleapis.com/css2?family=Arimo:wght@400;700&display=swap" rel="stylesheet">
<style>
:root{
  --page-bg:#e6e6e6;
  --sheet:#ffffff;
  --ink:#333333;
  --ink-soft:#555555;
  --brand-blue:#1f5fb0;
  --heading-blue:#0d5aa7;
  --navy:#0b3b7a;
  --nav-top:#5a5a5a;
  --nav-bottom:#3c3c3c;
  --rule:#d6d6d6;
  --button:#1565b4;
}
*{margin:0;padding:0;box-sizing:border-box}
html,body{width:1200px;height:805px;overflow:hidden;background:var(--page-bg);font-family:"Arimo",Arial,sans-serif;color:var(--ink)}
.sheet{position:absolute;left:180px;top:0;width:840px;height:805px;background:var(--sheet);box-shadow:0 0 4px rgba(0,0,0,.12)}
.abs{position:absolute;white-space:nowrap}
.brand-mark{left:270px;top:13px;width:62px;height:62px;background:var(--brand-blue)}
.brand-name{left:197px;top:76px;font-size:22px;color:#3a3a3a}
.brand-tag{left:247px;top:103px;font-size:11px;color:#3a3a3a}
.contact{font-size:10.5px;color:var(--ink)}
.contact svg{position:absolute}
.nav{position:absolute;left:189px;top:126px;width:822px;height:38px;background:linear-gradient(var(--nav-top),var(--nav-bottom))}
.nav a{position:absolute;top:14px;font-size:11px;color:#fff;text-decoration:none}
.hero{position:absolute;left:189px;top:164px;width:822px;height:318px;
  background:linear-gradient(180deg,#15181f 0%,#23262e 35%,#4a4a4c 62%,#2a2a2c 72%,#5e5748 88%,#3a3834 100%)}
.caption{position:absolute;left:189px;top:368px;width:427px;height:97px;background:rgba(20,20,20,.72);color:#fff}
.caption h2{position:absolute;left:30px;top:16px;font-size:14px;font-weight:400}
.caption p{position:absolute;left:30px;top:42px;width:390px;font-size:10.5px;line-height:22px;white-space:normal}
.dots{position:absolute;left:951px;top:463px;display:flex;gap:3px}
.dots span{width:8px;height:8px;background:#8a8a8a}
.dots span.on{background:var(--brand-blue)}
.about-title{left:195px;top:510px;font-size:15.5px;color:var(--heading-blue)}
.about-text{position:absolute;left:195px;top:537px;width:815px;font-size:10.5px;line-height:18px;color:var(--ink-soft)}
.divider{position:absolute;left:184px;top:614px;width:832px;height:4px;background:var(--rule)}
.foot-link{font-size:8.6px;color:#333;text-transform:uppercase}
.foot-head{font-size:9.2px;font-weight:700;color:var(--navy)}
.foot-sub{font-size:9.2px;color:var(--heading-blue)}
.email-box{position:absolute;left:607px;top:678px;width:198px;height:19px;border:1px solid #cfcfcf;font-size:8.2px;color:#888;padding:5px 8px}
.subscribe{position:absolute;left:727px;top:704px;width:78px;height:18px;background:var(--button);color:#fff;font-size:8.6px;text-align:center;line-height:18px}
.social{position:absolute;top:664px;width:12px;height:12px;border-radius:50%;background:var(--navy)}
.bottom-rule{position:absolute;left:184px;top:760px;width:832px;height:1px;background:var(--rule)}
.copyright{left:0;width:1200px;top:777px;text-align:center;font-size:8.6px;color:var(--navy)}
</style>
</head>
<body>
<div class="sheet"></div>

<header>
  <div class="abs brand-mark" aria-hidden="true"></div>
  <div class="abs brand-name">Halvencourt Law Group, LLP</div>
  <div class="abs brand-tag">Attorneys at Law</div>

  <div class="abs contact" style="left:795px;top:58px">
    <svg width="12" height="12" viewBox="0 0 12 12" style="left:0;top:1px"><path d="M2.5 1 L4.5 1 L5.2 3.6 L4 4.6 Q5 7 7.4 8 L8.4 6.8 L11 7.5 L11 9.5 Q10 11 8 10.8 Q1.5 9.5 1 3 Q1 1.5 2.5 1Z" fill="#222"/></svg>
    <span style="position:absolute;left:18px;top:0">(555) 014-1200</span>
  </div>
  <div class="abs contact" style="left:914px;top:58px">
    <svg width="11" height="11" viewBox="0 0 11 11" style="left:0;top:2px"><rect x="2.5" y="0.5" width="6" height="3" fill="#222"/><rect x="0" y="3.5" width="11" height="5" rx="1" fill="#222"/><rect x="2.5" y="7" width="6" height="4" fill="#fff" stroke="#222"/></svg>
    <span style="position:absolute;left:15px;top:0">(555) 014-1277</span>
  </div>
  <div class="abs contact" style="left:795px;top:87px">
    <svg width="11" height="9" viewBox="0 0 11 9" style="left:1px;top:2px"><rect x="0.5" y="0.5" width="10" height="8" fill="none" stroke="#222"/><path d="M0.5 0.5 L5.5 5 L10.5 0.5" fill="none" stroke="#222"/></svg>
    <span style="position:absolute;left:18px;top:0">info@halvencourtlaw-example.com</span>
  </div>
</header>

<nav class="nav">
  <a style="left:41px">HOME</a>
  <a style="left:129px">ABOUT HLG</a>
  <a style="left:240px">PRACTICE AREAS</a>
  <a style="left:388px">LINKS</a>
  <a style="left:474px">CONTACT</a>
</nav>

<section>
  <div class="hero" role="img" aria-label="Night skyline of a harbour city with lit towers, a bridge and water reflections"></div>
  <div class="caption">
    <h2>Halvencourt Law Group, LLP</h2>
    <p>provides quality legal representation to corporate as well as individual clients in the areas of business, corporate, securities, products liability, civil litigation</p>
  </div>
  <div class="dots"><span class="on"></span><span></span><span></span><span></span><span></span></div>
</section>

<main>
  <h1 class="abs about-title" style="font-weight:400">About the Firm</h1>
  <p class="about-text">Halvencourt Law Group, LLP takes pride in providing quality legal representation to its clients, whether they are large corporations, partnerships, or individuals.Our corporate clients benefit from the experience of our attorneys in the complex world of business, in addition to their keen legal skills. Our attorneys combine their thorough knowledge of the law with their personal experiences and backgrounds in business to provide each client with creative and unique solutions to litigation as well as transactional matters.</p>
</main>

<div class="divider"></div>

<footer>
  <div class="abs foot-link" style="left:196px;top:634px">Home</div>
  <div class="abs foot-link" style="left:196px;top:649px">About HLG</div>
  <div class="abs foot-link" style="left:196px;top:665px">Practice Areas</div>
  <div class="abs foot-link" style="left:196px;top:680px">Links</div>
  <div class="abs foot-link" style="left:196px;top:696px">Contact</div>

  <div class="abs foot-head" style="left:314px;top:640px">SERVICES</div>
  <div class="abs foot-link" style="left:314px;top:658px">Civil Litigation</div>
  <div class="abs foot-link" style="left:314px;top:673px">Employment Law</div>
  <div class="abs foot-link" style="left:314px;top:689px">Arbitration</div>
  <div class="abs foot-link" style="left:314px;top:704px">Mediation</div>
  <div class="abs foot-link" style="left:434px;top:658px">Corporate Securities</div>
  <div class="abs foot-link" style="left:434px;top:673px">Corporate Governance</div>
  <div class="abs foot-link" style="left:434px;top:689px">Mergers &amp; Acquisitions</div>
  <div class="abs foot-link" style="left:434px;top:704px">Business &amp; Commercial Law</div>
  <div class="abs foot-link" style="left:434px;top:720px">Contracts</div>

  <div class="abs foot-head" style="left:606px;top:640px">SUBSCRIBE FREE</div>
  <div class="abs foot-sub" style="left:606px;top:657px">RECENT UPDATES THROUGH YOUR EMAIL</div>
  <div class="email-box">ENTER YOUR EMAIL ID :</div>
  <div class="subscribe">SUBSCRIBE</div>

  <div class="abs foot-head" style="left:863px;top:640px">FOLLOW US</div>
  <span class="social" style="left:862px" aria-label="Social profile 1"></span>
  <span class="social" style="left:894px" aria-label="Social profile 2"></span>
  <span class="social" style="left:926px" aria-label="Social profile 3"></span>
  <span class="social" style="left:958px" aria-label="Social profile 4"></span>
  <span class="social" style="left:989px" aria-label="Social profile 5"></span>
  <div class="abs foot-link" style="left:867px;top:693px">Contact Us</div>
  <div class="abs foot-link" style="left:867px;top:708px">Disclaimer</div>
  <div class="abs foot-link" style="left:867px;top:724px">Privacy Policy</div>
  <div class="abs foot-link" style="left:867px;top:739px">Sitemap</div>

  <div class="bottom-rule"></div>
  <div class="abs copyright">© 2014. HALVENCOURT LAW GROUP. ALL RIGHTS RESERVED</div>
</footer>
</body>
</html>
```